Cover for nonfiction/memoir book "The Hidden Weather Within"

Revisions only please.

We're looking for a *nonfiction* *memoir* look that is consistent with other covers in that genre.

MUST HAVE:
- It must include the BACK COVER as it will be for print as well as an ebook.
- Title: The Hidden Weather Within
- TITLE MUST BE EASILY READ AT BRINDLECART THUMBNAIL SIZE
- Author name: Dorothea Quill
- At least one of the attached photos of Dorothea
- In COLOR
- The synopsis below
- Space for an endorsement

From the author: "I am looking for a cover that is eye catching and interesting or artistic, rather than just glamorous or pretty. If you like to edit the photos please do not completely remove the wrinkle between my eyebrows as I mention this in the book. It is okay if i look non conventional and my inner Aspie shows a little. The book is a little bit girly, and it would be good for the cover to reflect that, but mildly. No bright pink and purple designs. Please feel free to zoom in or crop the photos as you think works best"

SYNOPSIS (needs to go on the back cover)

The Hidden Weather Within is an acutely honest and often highly entertaining memoir by Dorothea Quill about life with Asperger's Syndrome. The book follows Dorothea in exploring her past and takes the reader with her on her journey to receiving and accepting her diagnosis. Instead of rehashing widely available Asperger's information, Dorothea focuses on discussing the thoughts, feelings and ideas that go along with being an Aspie, giving us a rare peek into what it really feels like to be a person on the spectrum. A must read for all those who enjoy deep personal stories or have a loved one on the spectrum that they wish to understand better.

The book dimensions will be 5x8 trade paperback and 6x9 hardcover (plus 0.25 bleed margin on all sizes - for both sizes).
Here is some more information from the publisher on cover requirements:

"I've attached a sample of both a paperback and hardcover size. Note that the spine width will be different depending on the final length of the book, so it won't be exact. That said, the front and back covers, and the flaps (for the hardcover) will always be the same as shown.
For deliverables, we need the following:

a Creative Suite 6 or earlier native .PSD (Photoshop), .ID (InDesign), or .AI (Illustrator) file. Creative Cloud files cannot be used and will not be accepted.
final file must include layered objects, and cannot be one 'background' image
Final files must be in CMYK color mode, 300dpi minimum
Total Ink saturation must be no more than 240% on any part of the cover. "True" black should use the following CMYK values: 60/40/40/100.
Fonts used in creation of the cover must be either A) embedded or B) sent with the final file
Vector art is preferred for scaling purposes"

Target Market(s)

Women of all ages. People who like psychology and personal stories.
Also parents and family members who may have a loved one on the Autism spectrum.

Requirements
Nice to have
• Bright green new leaves and greenery are good but not necessary.

```html
<!DOCTYPE html>
<html lang="en">
<head>
<meta charset="utf-8">
<title>The Hidden Weather Within — Cover Spread</title>
<link rel="stylesheet" href="https://fonts.googleapis.com/css2?family=Pacifico&family=Cinzel:wght@400;600&family=Libre+Baskerville:wght@400;700&family=Open+Sans:wght@400;600&display=swap">
<style>
  :root {
    --page-bg: #ffffff;
    --sky-light: #e7e2cf;
    --sky-teal: #9dbcb6;
    --haze: #d9cfa8;
    --field-gold: #b8a064;
    --field-deep: #9c8449;
    --dress-dark: #4e3a3a;
    --cream: #f4efe2;
    --ink-brown: #4f4130;
    --ink-soft: #5c5244;
    --band-mauve: #9b5a62;
    --band-teal: #3f6f6d;
    --band-olive: #8a7b3d;
    --title-white: #fbf8f0;
    --author-cream: #f3ead6;
  }
  * { margin: 0; padding: 0; box-sizing: border-box; }
  html, body {
    width: 1200px; height: 667px; overflow: hidden;
    background: var(--page-bg);
  }
  .spread {
    position: absolute; left: 202px; top: 53px;
    width: 796px; height: 561px;
    display: flex;
  }
  .panel-face { position: relative; height: 100%; overflow: hidden; }
  .back-cover { width: 373px; }
  .spine { width: 50px; }
  .front-cover { width: 373px; }

  .field-backdrop {
    position: absolute; inset: 0;
    background: linear-gradient(180deg,
      var(--sky-light) 0%, var(--sky-teal) 22%, var(--haze) 34%,
      var(--field-gold) 50%, var(--field-deep) 100%);
  }
  .portrait-backdrop {
    position: absolute; inset: 0;
    background:
      radial-gradient(ellipse 45% 40% at 62% 30%, #e9cf9f 0%, rgba(233,207,159,0) 70%),
      radial-gradient(ellipse 55% 35% at 70% 80%, var(--dress-dark) 0%, rgba(78,58,58,0) 75%),
      linear-gradient(180deg, var(--sky-light) 0%, var(--sky-teal) 20%, var(--haze) 36%, var(--field-gold) 55%, var(--field-deep) 100%);
  }

  /* back cover */
  .back-headline {
    position: absolute; top: 66px; left: 40px; right: 40px;
    text-align: center;
    font-family: "Libre Baskerville", Georgia, serif;
    font-weight: 400; font-size: 10px; line-height: 1.5;
    letter-spacing: 0.3px;
    color: var(--ink-brown);
  }
  .back-headline strong { font-weight: 700; }
  .back-panel {
    position: absolute; left: 0; width: 322px;
    background: var(--cream);
    padding: 9px 14px 8px 14px;
    font-family: "Libre Baskerville", Georgia, serif;
    color: var(--ink-soft);
  }
  .back-panel p { font-size: 7.2px; line-height: 1.55; }
  .back-panel cite {
    display: block; text-align: right; margin-top: 5px;
    font-style: normal; font-size: 7.4px; letter-spacing: 0.4px;
    font-variant: small-caps;
  }
  .back-panel::after {
    content: ""; position: absolute; left: 0; right: 0; bottom: -6px; height: 6px;
  }
  .synopsis--opening { top: 212px; }
  .synopsis--opening::after { background: var(--band-mauve); }
  .synopsis--closing { top: 298px; }
  .synopsis--closing::after { background: var(--band-teal); }
  .endorsement { top: 396px; }
  .endorsement::after { background: var(--band-olive); }
  .isbn-box {
    position: absolute; left: 275px; top: 490px;
    width: 84px; height: 58px; background: #ffffff;
  }

  /* spine */
  .spine-text {
    position: absolute; left: 0; width: 50px;
    writing-mode: vertical-rl;
    display: flex; align-items: center; justify-content: center;
  }
  .spine-author {
    top: 22px; height: 140px;
    font-family: "Cinzel", Georgia, serif; font-size: 11px;
    letter-spacing: 2px; color: var(--ink-brown);
  }
  .spine-title {
    top: 190px; height: 340px;
    font-family: "Pacifico", cursive; font-size: 20px;
    color: var(--title-white);
    text-shadow: 0 1px 2px rgba(60,45,25,0.35);
  }

  /* front cover */
  .front-title {
    position: absolute; left: 52px; top: 302px;
    font-family: "Pacifico", cursive;
    color: var(--title-white);
    text-shadow: 0 2px 4px rgba(60,45,25,0.4);
    line-height: 1.05;
  }
  .front-title .title-major { display: block; font-size: 50px; }
  .front-title .title-minor {
    display: block; padding-left: 150px; margin-top: -4px;
    font-family: "Open Sans", Arial, sans-serif; font-weight: 600;
    font-size: 16px; letter-spacing: 1px;
    text-shadow: 0 1px 3px rgba(60,45,25,0.4);
  }
  .front-author {
    position: absolute; left: 0; right: 0; top: 496px;
    text-align: center; padding-left: 60px;
    font-family: "Cinzel", Georgia, serif; font-size: 21px;
    letter-spacing: 2.5px; color: var(--author-cream);
    text-shadow: 0 1px 3px rgba(60,45,25,0.4);
  }
</style>
</head>
<body>
  <main class="spread">
    <section class="panel-face back-cover">
      <div class="field-backdrop" role="img" aria-label="Faded photograph of a sunlit grassy meadow under a pale teal sky"></div>
      <h2 class="back-headline">An acutely honest, often highly entertaining<br>memoir of life with <strong>Asperger's Syndrome</strong></h2>

      <div class="back-panel synopsis--opening">
        <p><em>The Hidden Weather Within</em> is an acutely honest and often highly entertaining memoir by Dorothea Quill about life with Asperger's Syndrome. The book follows Dorothea in exploring her past and takes the reader with her on her journey to receiving and accepting her diagnosis.</p>
      </div>
      <div class="back-panel synopsis--closing">
        <p>Instead of rehashing widely available Asperger's information, Dorothea focuses on discussing the thoughts, feelings and ideas that go along with being an Aspie, giving us a rare peek into what it really feels like to be a person on the spectrum. A must read for all those who enjoy deep personal stories or have a loved one on the spectrum that they wish to understand better.</p>
      </div>
      <blockquote class="back-panel endorsement">
        <p>Tender, clever and surprisingly light on its feet. A book for anyone who has ever felt a little out of step, and for those who want to walk beside them with more understanding.</p>
        <cite>~ Lorem Ipsum ~</cite>
      </blockquote>

      <div class="isbn-box"></div>
    </section>

    <section class="panel-face spine">
      <div class="field-backdrop" role="img" aria-label="Continuation of the meadow and sky photograph along the spine"></div>
      <span class="spine-text spine-author">DOROTHEA QUILL</span>
      <span class="spine-text spine-title">The Hidden Weather Within</span>
    </section>

    <section class="panel-face front-cover">
      <div class="portrait-backdrop" role="img" aria-label="Photograph of the author sitting in a golden meadow in a floral dress, gazing upward against a pale teal sky"></div>
      <h1 class="front-title">
        <span class="title-major">The Hidden</span>
        <span class="title-major">Weather</span>
        <span class="title-minor">within</span>
      </h1>
      <p class="front-author">DOROTHEA QUILL</p>
    </section>
  </main>
</body>
</html>
```